Internationally renowned Business Coach and Public Speaker needs new Website

I need a website to further support and expand my personal brand - I am a well known entrepreneur, business coach and public speaker on the thema of 'Business Acceleration' and I regularly write articles and have written a popular managementbook on this thema. I would like a new, visually strong and exciting website to explain my background and added value as a business coach and keynote speaker. As a reference I would like to point out the website of Tor Velund (www.torvelund.example).

Target Market(s)

top CEO's of international companies

Industry/Entity Type

Business

Number of Pages Required

1 page

Requirements
Nice to have
• us as a reference: www.torvelund.example

```html
<!DOCTYPE html>
<html lang="en">
<head>
<meta charset="utf-8">
<title>Joren Valkhof – Business Acceleration</title>
<link rel="stylesheet" href="https://fonts.googleapis.com/css2?family=Michroma&family=Arimo:wght@400;700&display=swap">
<style>
:root{
  --page:#c6c6c6;
  --red:#e0262a;
  --bright:#ff1a1a;
  --panel:#e05252;
  --ink:#222;
  --muted:#555;
  --card-head:#c9d3e2;
  --purple:#8b3a8f;
  --white:#fff;
}
*{box-sizing:border-box;margin:0;padding:0}
html,body{width:819px;height:1200px;overflow:hidden}
body{background:var(--page);font-family:"Arimo",Arial,sans-serif;color:var(--ink);position:relative}
.abs{position:absolute}
.display{font-family:"Michroma",sans-serif}

.brand{left:58px;top:13px;display:flex;align-items:center;gap:6px}
.brand-dot{width:34px;height:34px;border-radius:50%;background:var(--red)}
.brand-name{font-size:8px;font-weight:700;color:#777;line-height:9px;width:60px}

.nav{left:190px;top:26px;display:flex;font-size:7.5px;font-variant:small-caps;font-size:9px;color:#333;gap:6px;align-items:center}
.nav a{color:#333;text-decoration:none}
.nav .current{color:var(--red);text-decoration:underline;display:flex;align-items:center;gap:3px}
.nav .current::before{content:"";width:7px;height:7px;border:2px solid var(--red);border-radius:50%}
.nav .sep{color:#333}

.social{left:566px;top:23px;display:flex;gap:5px}
.social span{width:16px;height:16px;background:#333;display:block}

.hero{left:51px;top:62px;width:615px;height:308px;background:radial-gradient(circle at 65% 40%,#c49a86 0,#8a6f78 22%,transparent 45%),linear-gradient(110deg,#4e3f8f 0%,#7a64b6 35%,#d7a0a4 70%,#f08a8c 100%);box-shadow:0 2px 4px rgba(0,0,0,.3)}
.hero-copy{left:10px;top:62px;width:284px;text-align:center;color:var(--white)}
.hero-title{font-size:22px;text-decoration:underline;text-underline-offset:4px;font-variant:small-caps;letter-spacing:2px}
.hero-sub{font-size:13px;letter-spacing:3px;margin-top:8px}
.hero-text{font-size:6.5px;line-height:11px;margin-top:12px;letter-spacing:1px;text-transform:uppercase}
.dots{left:333px;top:292px;display:flex;gap:4px}
.dots i{width:7px;height:7px;border-radius:50%;background:#bbb;display:block}
.dots i:first-child{background:var(--red)}

.panel{background:var(--panel);box-shadow:0 2px 4px rgba(0,0,0,.35);color:var(--ink);text-align:center}
.signup{left:586px;top:214px;width:206px;height:179px;padding-top:12px}
.signup h2{font-size:16px;font-weight:400;text-decoration:underline}
.signup .lead{font-size:9px;margin-top:3px}
.signup .lead b{font-weight:400;color:#2a2aa0}
.signup .note{font-size:7px;color:var(--white);line-height:12px;margin-top:5px}
.field{width:171px;height:15px;border:1px solid var(--bright);margin:6px auto 0;font-size:6px;color:var(--white);text-align:left;padding:4px 4px}
.btn{background:var(--bright);color:var(--white);font-size:6.5px;border:1px solid var(--white);display:inline-block;padding:3px 13px}
.signup .btn{margin-top:13px}

.card{top:392px;width:164px;height:198px;background:var(--white);border-radius:3px;box-shadow:0 2px 4px rgba(0,0,0,.3);text-align:center;overflow:hidden}
.card h3{height:24px;background:var(--card-head);color:var(--red);font-family:"Michroma",sans-serif;font-weight:400;font-variant:small-caps;font-size:11px;line-height:24px}
.card .photo{height:96px}
.card p{font-size:6.5px;color:var(--red);line-height:9px;padding:11px 14px 0;height:49px}
.card .btn{position:absolute;right:16px;bottom:12px;padding:2px 9px;border:none}

.power{left:586px;top:426px;width:206px;height:114px;padding-top:11px}
.power h4{font-size:9.5px}
.power p{font-size:7.5px;color:var(--white);line-height:10px;margin-top:2px}
.power .btn{margin-top:10px;padding:3px 28px}
.story{left:586px;top:542px;width:206px;height:213px;background:linear-gradient(180deg,#7a7a7a,#bdbdbd);box-shadow:0 2px 4px rgba(0,0,0,.35);border-bottom:4px solid var(--panel)}
.story p{position:absolute;left:0;right:0;bottom:10px;text-align:center;color:var(--white);font-size:11px;line-height:15px}
.story p span{color:var(--bright)}

.call{left:586px;top:787px;width:206px;height:113px;padding-top:9px;color:var(--white)}
.call .icon{width:56px;height:56px;margin:0 auto;border-radius:50%;background:var(--bright);border:2px solid var(--white);display:flex;align-items:center;justify-content:center}
.call .small{font-size:9.5px;margin-top:7px}
.call .num{font-size:15px;font-weight:700}

.expert{left:51px;top:614px;width:531px;height:167px;background:linear-gradient(180deg,#c8c8c8 85%,#d9b3b3 100%);box-shadow:0 2px 4px rgba(0,0,0,.3);text-align:center;padding-top:24px}
.expert h2{font-family:"Michroma",sans-serif;font-weight:400;font-size:14px;color:var(--red);letter-spacing:2px;text-decoration:underline}
.expert p{font-size:6.5px;line-height:12.5px;margin-top:10px}
.expert .actions{display:flex;justify-content:center;gap:10px;margin-top:11px}
.expert .btn{font-size:7.5px;padding:0;width:100px;height:26px;display:flex;align-items:center;justify-content:center;border:1px solid #900;line-height:9px}

.testi-title{left:0;width:625px;top:808px;text-align:center;font-variant:small-caps;font-size:13px;text-decoration:underline}
.avatar{left:278px;top:841px;width:62px;height:62px;border-radius:50%;border:2px solid var(--purple);padding:3px}
.avatar div{width:100%;height:100%;border-radius:50%;background:linear-gradient(#8a8a8a,#c0c0c0)}
.arrow{top:860px}
.testi-text{left:114px;top:927px;width:397px;font-size:6.5px;line-height:8.8px}

.companies{left:51px;top:1006px;width:531px;height:174px;background:var(--white);box-shadow:0 2px 4px rgba(0,0,0,.3);text-align:center;padding-top:16px}
.companies h2{font-family:"Michroma",sans-serif;font-weight:400;font-size:13px;color:var(--red);letter-spacing:2px;text-decoration:underline;font-variant:small-caps}
.logo-box{top:59px;width:132px;height:84px;background:var(--page);font-family:"Michroma",sans-serif;font-variant:small-caps;color:var(--red);font-size:13px;letter-spacing:1px;text-decoration:underline;display:flex;align-items:center;justify-content:center}
.round{top:86px;width:30px;height:30px;border-radius:50%;background:#bdbdbd}
</style>
</head>
<body>

<header>
  <div class="brand abs"><span class="brand-dot"></span><span class="brand-name">Veltrix Business Accelerators</span></div>
  <nav class="nav abs">
    <a class="current" href="#">Home</a><span class="sep">|</span>
    <a href="#">Services</a><span class="sep">|</span>
    <a href="#">Impact Stories</a><span class="sep">|</span>
    <a href="#">Media</a><span class="sep">|</span>
    <a href="#">About</a><span class="sep">|</span>
    <a href="#">Resources</a><span class="sep">|</span>
    <a href="#">Contact</a>
  </nav>
  <div class="social abs" aria-label="Social links"><span></span><span></span><span></span><span></span><span></span></div>
</header>

<section class="hero abs" role="img" aria-label="Portrait photo of Joren Valkhof smiling against a soft purple and pink backdrop">
  <div class="hero-copy abs">
    <div class="hero-title display">Success</div>
    <div class="hero-sub display">JUST AHEAD</div>
    <p class="hero-text display">We become what we think about most of the time,<br>and that's the strangest secret.<br>Achieve your goals in life and in business<br>with Joren's help you can.</p>
  </div>
  <div class="dots abs"><i></i><i></i><i></i><i></i><i></i></div>
</section>

<aside class="signup panel abs">
  <h2>Sign Up</h2>
  <p class="lead">Now to &nbsp;Get <b>JOREN'S</b> EXCLUSIVE</p>
  <p class="note">Sign Up Now To Get Joren's EXCLUSIVE Special<br>Report on Goal Getting and Taking Action!</p>
  <div class="field">First Name</div>
  <div class="field">Last Name</div>
  <div class="field">Email</div>
  <span class="btn">Sign Up Now!</span>
</aside>

<article class="card abs" style="left:51px">
  <h3>Keynote Speaking</h3>
  <div class="photo" role="img" aria-label="Joren speaking on stage to an audience under pink lights" style="background:linear-gradient(#c67ad0,#6b3a6e)"></div>
  <p>A highly acclaimed international speaker, Joren Valkhof is the flash of inspiration that moves you to action.</p>
  <span class="btn">Know More</span>
</article>
<article class="card abs" style="left:235px">
  <h3>Signature Programs</h3>
  <div class="photo" role="img" aria-label="Joren presenting with open hands against a violet background" style="background:linear-gradient(90deg,#5a2f7a,#d68fe0)"></div>
  <p>Joren Valkhof's signature programs empower individuals, businesses and organizations with the skills, attitude...</p>
  <span class="btn">Know More</span>
</article>
<article class="card abs" style="left:418px">
  <h3>Success Coaching</h3>
  <div class="photo" role="img" aria-label="Black and white portrait of Joren beside the word Standardisation" style="background:linear-gradient(90deg,#050505 45%,#6a6a6a)"></div>
  <p>A multitalented and charismatic speaker, Joren Valkhof's knowledge and intrinsic understanding of business strategy and psychological drivers</p>
  <span class="btn">Know More</span>
</article>

<aside class="power panel abs">
  <h4>JOREN'S DAILY POWER MESSAGE:</h4>
  <p>Need motivation? Sign-up for Tor's Daily Power<br>Message to give you that boost you need!</p>
  <div class="field">First Name</div>
  <span class="btn">Submit</span>
</aside>
<aside class="story abs" role="img" aria-label="Black and white photo of Joren speaking with a microphone">
  <p><span>Click here</span> to learn more about<br>Joren Valkhof's story</p>
</aside>

<aside class="call panel abs">
  <div class="icon">
    <svg width="28" height="28" viewBox="0 0 24 24" aria-hidden="true"><path fill="#fff" d="M6.6 10.8a15 15 0 0 0 6.6 6.6l2.2-2.2c.3-.3.7-.4 1-.2 1.1.4 2.3.6 3.6.6.6 0 1 .4 1 1V20c0 .6-.4 1-1 1A17 17 0 0 1 3 4c0-.6.4-1 1-1h3.5c.6 0 1 .4 1 1 0 1.3.2 2.5.6 3.6.1.3 0 .7-.2 1z"/></svg>
  </div>
  <div class="small">Call Us Now</div>
  <div class="num">+1 555 014 2290</div>
</aside>

<section class="expert abs">
  <h2>EXPERT IN HUMAN EMPOWERMENT</h2>
  <p>Serial entrepreneur, business strategist, personal development facilitator and international speaker.<br>Joren Valkhof has made an impact on over 200,000 people the world over.<br>He is renowned for helping people achieve their potential and helping people<br>create revenues (not profit) of over 1 million in as little as six months from nothing.</p>
  <div class="actions">
    <span class="btn">View Joren Valkhof's<br>Upcoming Events</span>
    <span class="btn">Start Learning Today</span>
  </div>
</section>

<h2 class="testi-title abs">Testimonials</h2>
<svg class="arrow abs" style="left:68px" width="26" height="34" viewBox="0 0 26 34" aria-hidden="true"><path d="M22 2 6 17l16 15" fill="none" stroke="var(--purple)" stroke-width="5"/></svg>
<svg class="arrow abs" style="left:543px" width="26" height="34" viewBox="0 0 26 34" aria-hidden="true"><path d="M4 2l16 15L4 32" fill="none" stroke="var(--purple)" stroke-width="5"/></svg>
<div class="avatar abs"><div role="img" aria-label="Client portrait photo"></div></div>
<p class="testi-text abs">A specific learning disability that is neurological in origin. It is characterized by difficulties with accurate and/or fluent word recognition, and by poor spelling and decoding abilities. These difficulties result from a deficit in the phonological component of language that is often unexpected in relation to other cognitive abilities and the provision of effective classroom instruction. Secondary consequences include problems in reading comprehension and reduced reading experience that can impede growth of vocabulary and background knowledge.</p>

<section class="companies abs">
  <h2>Companies Joren has worked with</h2>
  <span class="round abs" style="left:9px"><svg width="30" height="30" viewBox="0 0 30 30" aria-hidden="true"><path d="M18 8l-7 7 7 7" fill="none" stroke="#fff" stroke-width="4"/></svg></span>
  <div class="logo-box abs" style="left:54px">Company 1</div>
  <div class="logo-box abs" style="left:199px">Company 2</div>
  <div class="logo-box abs" style="left:344px">Company 3</div>
  <span class="round abs" style="left:489px"><svg width="30" height="30" viewBox="0 0 30 30" aria-hidden="true"><path d="M12 8l7 7-7 7" fill="none" stroke="#fff" stroke-width="4"/></svg></span>
</section>

</body>
</html>
```